Real estate company needs a card that makes you say WOW!

We need an awesome business card for our real estate company, Stonebrook Realty Partners of Chicago, that will stand out from the crowd. We specialize in buying and selling real estate, property management, and real estate investments (Flips & Rentals). On the business card, I need the following:

- Our logo
- Services
- My name & contact info (Derek Ollanby, 630-517-2946, Derek@StonebrookRPC.com)
- My title (Director of Acquisitions)
- StonebrookRPC.com

I attached an EPS file of our logo. Let me know if you have any questions. Thank you in advance!

```html
<!DOCTYPE html>
<html lang="en">
<head>
<meta charset="utf-8">
<title>Stonebrook Realty Partners of Chicago – Business Card</title>
<link rel="stylesheet" href="https://fonts.googleapis.com/css2?family=Tinos:wght@400;700&display=swap">
<style>
  :root {
    --page-bg: #d2d2d2;
    --blue-dark: #0a5690;
    --blue-mid: #1477bf;
    --blue-text: #10609f;
    --white: #ffffff;
    --rule-grey: #8a8a8a;
  }
  * { margin: 0; padding: 0; box-sizing: border-box; }
  html, body {
    width: 1200px;
    height: 1000px;
    overflow: hidden;
    background: var(--page-bg);
  }
  .card {
    position: absolute;
    overflow: hidden;
    font-family: "Tinos", "Times New Roman", serif;
  }
  .blue-fill {
    background: linear-gradient(90deg, var(--blue-dark) 0%, var(--blue-mid) 50%, var(--blue-dark) 100%);
  }

  /* Company name */
  .company-name {
    position: absolute;
    left: 0; right: 0;
    text-align: center;
    font-family: "Tinos", "Times New Roman", serif;
    font-weight: 400;
    font-size: 30px;
    line-height: 1;
  }
  .card-front .company-name { top: 190px; color: var(--white); }

  /* Front */
  .card-front {
    left: 93px; top: 61px;
    width: 693px; height: 405px;
  }
  .services {
    position: absolute;
    left: 0; right: 0; top: 262px;
    list-style: none;
    text-align: center;
    color: var(--white);
    font-size: 21px;
  }
  .services li { height: 44px; }
  .services li::before { content: "• "; }

  /* Back */
  .card-back {
    left: 434px; top: 546px;
    width: 704px; height: 410px;
    background: var(--white);
  }
  .back-band {
    position: absolute;
    left: 0; top: 0;
    width: 704px; height: 410px;
  }
  .card-back .company-name { top: 100px; color: var(--blue-text); }
  .holder {
    position: absolute;
    left: 78px; top: 308px;
    color: var(--white);
  }
  .holder-name { font-size: 22px; font-weight: 700; line-height: 1.2; }
  .holder-title { font-size: 21px; line-height: 1.3; }
  .divider {
    position: absolute;
    left: 313px; top: 299px;
    width: 1px; height: 83px;
    background: rgba(255,255,255,0.75);
  }
  .contacts {
    position: absolute;
    left: 336px; top: 296px;
    list-style: none;
    color: var(--white);
    font-size: 21px;
  }
  .contacts li {
    display: flex;
    align-items: center;
    height: 31px;
  }
  .contacts svg { width: 16px; height: 16px; margin-right: 13px; flex: none; }
</style>
</head>
<body>

<section class="card card-front blue-fill">
  <p class="company-name">Stonebrook Realty Partners of Chicago</p>
  <ul class="services">
    <li>Buying and Selling Real Estate</li>
    <li>Property Management</li>
    <li>Real Estate Investments (Flips &amp; Rentals)</li>
  </ul>
</section>

<section class="card card-back">
  <svg class="back-band" viewBox="0 0 704 410" aria-hidden="true">
    <defs>
      <linearGradient id="bandBlue" x1="0" x2="1" y1="0" y2="0">
        <stop offset="0" stop-color="#0a5690"/>
        <stop offset="0.5" stop-color="#1477bf"/>
        <stop offset="1" stop-color="#0a5690"/>
      </linearGradient>
    </defs>
    <path d="M0 154 Q352 330 704 154 L704 410 L0 410 Z" fill="url(#bandBlue)"/>
    <path d="M0 154 Q352 330 704 154" fill="none" stroke="#8a8a8a" stroke-width="6"/>
  </svg>

  <p class="company-name">Stonebrook Realty Partners of Chicago</p>

  <div class="holder">
    <p class="holder-name">Derek Ollanby</p>
    <p class="holder-title">Director of Acquisitions</p>
  </div>

  <div class="divider"></div>

  <ul class="contacts">
    <li>
      <svg viewBox="0 0 16 16" aria-hidden="true"><rect x="3" y="1" width="10" height="14" rx="1.5" fill="#fff"/><rect x="5" y="3" width="6" height="4" fill="#1477bf"/><rect x="5" y="9" width="2" height="1.5" fill="#1477bf"/><rect x="9" y="9" width="2" height="1.5" fill="#1477bf"/><rect x="5" y="12" width="2" height="1.5" fill="#1477bf"/><rect x="9" y="12" width="2" height="1.5" fill="#1477bf"/></svg>
      630-517-2946
    </li>
    <li>
      <svg viewBox="0 0 16 16" aria-hidden="true"><rect x="1" y="3.5" width="14" height="9.5" fill="none" stroke="#fff" stroke-width="1.2"/><path d="M1 3.5 L8 9 L15 3.5" fill="none" stroke="#fff" stroke-width="1.2"/></svg>
      Derek@StonebrookRPC.com
    </li>
    <li>
      <svg viewBox="0 0 16 16" aria-hidden="true"><circle cx="8" cy="8" r="6.5" fill="none" stroke="#fff" stroke-width="1.3"/><ellipse cx="8" cy="8" rx="2.8" ry="6.5" fill="none" stroke="#fff" stroke-width="1.1"/><path d="M1.5 8 H14.5" stroke="#fff" stroke-width="1.1"/></svg>
      www.StonebrookRPC.com
    </li>
  </ul>
</section>

</body>
</html>
```